Travel Business Card

Hello. I am an award-winning travel advisor in Sydney, Australia seeking new business cards reflecting a unique style. Words to describe the design I'm seeking - Contemporary, Artsy, Vibrant, Soulful, Journey.

I loved this'Absolut' design and have created a few concepts to guide you for the back of the bus card. Feel free to use your own imagination...
maybe use elements of a Venetian mask or City (Icon), Cruise Ship, Sunshine, Beach/ Beach Hut, Buddha (Spiritual), Lotus or Palm Tree (Nature), Magic Carpet (Middle East), Whale or Waves, or enhance the pencil sketch I did...

Remember. The design should look high-end and fashionable.

Looking forward to hearing from you.
My email is miriam@plenvoritrips.example.

Many thanks.

```html
<!DOCTYPE html>
<html lang="en">
<head>
<meta charset="utf-8">
<title>Miriam Vester – Travel Advisor Business Card</title>
<link href="https://fonts.googleapis.com/css2?family=Open+Sans:ital,wght@0,400;0,600;0,700;1,400&family=Raleway:wght@700&display=swap" rel="stylesheet">
<style>
  :root {
    --backdrop: #cdd1d2;
    --card: #ffffff;
    --plum: #7b4a78;
    --teal: #6fd3c8;
    --mint: #a9e3d8;
    --cream: #f6f1cf;
    --coral: #f19a86;
    --lime: #c9e04a;
  }
  html, body {
    margin: 0;
    width: 1200px;
    height: 1000px;
    overflow: hidden;
    background: var(--backdrop);
  }
  .canvas {
    position: relative;
    width: 1200px;
    height: 1000px;
  }
  .card {
    position: absolute;
    top: 239px;
    width: 301px;
    height: 507px;
    overflow: hidden;
    box-shadow: 0 2px 6px rgba(0,0,0,0.12);
  }
  .card--front {
    left: 290px;
    background: var(--card);
    color: var(--plum);
    font-family: "Open Sans", Arial, sans-serif;
  }
  .card--back {
    left: 656px;
    background:
      radial-gradient(circle at 63% 18%, #ffffff 0 6%, transparent 7%),
      radial-gradient(ellipse at 60% 45%, var(--cream) 0 25%, transparent 55%),
      linear-gradient(160deg, var(--coral) 0%, var(--mint) 35%, #b8d9c4 60%, var(--teal) 80%, var(--lime) 100%);
  }
  .card--front > * {
    position: absolute;
    left: 42px;
    margin: 0;
    white-space: nowrap;
  }
  .holder-name {
    top: 61px;
    font-family: "Raleway", "Open Sans", sans-serif;
    font-weight: 700;
    font-size: 22px;
    letter-spacing: 0;
  }
  .holder-role { top: 95px; font-size: 13.5px; font-weight: 600; }
  .divider {
    top: 128px;
    width: 216px;
    height: 0;
    border-top: 2px solid var(--teal);
  }
  .licence { top: 146px; font-size: 11px; font-style: italic; line-height: 14px; }
  .contact {
    top: 201px;
    font-size: 13.5px;
    font-weight: 700;
    line-height: 21.8px;
    list-style: none;
    padding: 0;
  }
  .website { top: 331px; font-size: 13.5px; font-weight: 700; letter-spacing: 0.3px; }
  .experience { top: 387px; font-size: 12px; line-height: 14px; }
  .award { top: 430px; font-size: 11.5px; font-weight: 700; line-height: 14px; }
  .award-body { top: 459px; font-size: 7px; font-style: italic; }
  .corner-dot {
    left: 146px;
    top: 489px;
    width: 3px;
    height: 3px;
    border-radius: 50%;
    background: var(--teal);
  }
</style>
</head>
<body>
<main class="canvas">
  <section class="card card--front" aria-label="Business card front">
    <h1 class="holder-name">MIRIAM VESTER</h1>
    <p class="holder-role">Travel Advisor</p>
    <div class="divider"></div>
    <p class="licence">LIC. NO. 4QX20917<br>ABN. 12 345 678 910</p>
    <ul class="contact">
      <li>M. 0400 555 218</li>
      <li>F. 02 5550 7431</li>
      <li>E. TRAVEL@MVESTER.EXAMPLE</li>
      <li>A. PO BOX 512,</li>
      <li>ELMWOOD RIDGE, NSW 2190</li>
    </ul>
    <p class="website">WWW. MVESTER.EXAMPLE</p>
    <p class="experience">OVER 16 YEARS EXPERIENCE<br>LEISURE &amp; CORPORATE</p>
    <p class="award">AUSTRALIAN CRUISE CONSULTANT<br>OF THE YEAR, 2008</p>
    <p class="award-body">OCEAN VOYAGES TRAVEL ALLIANCE (OVTA)</p>
    <span class="corner-dot"></span>
  </section>
  <section class="card card--back" role="img"
    aria-label="Illustration: tropical leaves framing a city skyline, a sun, a plane trailing a pink ribbon and flowing waves in pastel tones"></section>
</main>
</body>
</html>
```